Website For Custom Home Builder

-Very elegant and simple design as I am a high end custom home builder.
-I build homes $2 million to $10 million range so the website needs to reflect the level of home that I build.
-Attached are photos of homes I have built to use as well as my logo.
-I need final design to be in layered format so my local guy can edit if he needs to.

3 Page Design
1. HomePage:
-logo, some photos,
-“Building beautiful custom homes in Indianapolis for over 20 years”
2. AboutPage:
-Wade Holloran has been building stunning custom homes in the Indianpolis area for over 20 years. As a small boutique building company we only build a handful of homes a year in order to offer our clients the personal attention that their homes deserve. It's this attention to detail that makes our client experience and final product something special and unique.
- family photo
3. ContactPage:
-office photo
-317-552-7190
-wade@whcrafted.com
-415 North Fernmill Rd, Suite 308, Carmel IN 46033

Target Market(s)

Very high end clients looking to build $2 million to $10 million homes.

Industry/Entity Type

Residential high end custom home builder/construction

Coding

Coded - Design and coding required

Number of Pages Required

3 page

Requirements
Must have
• Very simple and elegant design that represents the high end homes that I build.
Nice to have
Should not have
• Should NOT have a lot of clutter or be a very busy page from a design perspective.

```html
<!DOCTYPE html>
<html lang="en">
<head>
<meta charset="utf-8">
<title>Wade Holloran Custom Homes</title>
<link href="https://fonts.googleapis.com/css2?family=Nunito+Sans:wght@300;400;600;700&display=swap" rel="stylesheet">
<style>
:root{
  --brown-dark:#2d170c;
  --accent:#a2521c;
  --accent-line:#b8703f;
  --text:#2b2b2b;
  --muted:#9a9a9a;
  --field:#f3f3f3;
  --white:#ffffff;
}
*{margin:0;padding:0;box-sizing:border-box}
html,body{width:1200px;height:3235px;overflow:hidden;background:var(--white)}
body{position:relative;font-family:"Nunito Sans",sans-serif;color:var(--text)}
.abs{position:absolute}
.brand{display:flex;align-items:center;gap:10px;font-weight:600;color:var(--text);white-space:nowrap}
.brand-mark{width:14px;height:14px;background:currentColor}

/* header */
.site-header{left:0;top:0;width:1200px;height:124px;background:var(--white)}
.site-header .brand{left:113px;top:48px;font-size:24px}
.nav{left:652px;top:58px;display:flex;gap:40px;font-size:16px}
.nav a{color:var(--text);text-decoration:none}
.nav a.active{text-decoration:underline;text-underline-offset:4px;font-weight:600}
.btn{display:flex;align-items:center;justify-content:center;border-radius:6px;font-size:16px;text-decoration:none}
.btn-accent{background:var(--accent);color:var(--white)}
.enquire{left:939px;top:48px;width:129px;height:42px}

/* hero */
.hero{left:0;top:124px;width:1200px;height:560px;overflow:hidden}
.hero-left{left:0;top:0;width:700px;height:560px;background:linear-gradient(180deg,#4a3a2c 0%,#6a5238 45%,#1f3e6a 75%,#123064 100%)}
.hero-right{left:0;top:0;width:1200px;height:560px;clip-path:polygon(690px 0,1200px 0,1200px 560px,525px 560px);background:linear-gradient(180deg,#c9a178 0%,#7f5a3c 40%,#4c3a2a 65%,#41532a 85%,#334520 100%)}
.hero-divider{left:0;top:0}
.hero-title{left:113px;top:155px;color:var(--white);font-weight:300;font-size:72px;line-height:1;letter-spacing:-1px}
.hero-sub{left:113px;top:228px;color:var(--white);font-weight:300;font-size:30px;letter-spacing:14px}
.hero-tag{left:115px;top:278px;color:var(--white);font-size:20px;line-height:29px;width:460px}
.get-started{left:115px;top:354px;width:152px;height:42px;font-size:16px}

/* about */
.about{left:-8px;top:656px;width:1216px;height:610px;background:var(--brown-dark);border:8px solid var(--white);border-bottom:none;border-radius:56px 56px 0 0}
.section-title{font-weight:400;font-size:36px;line-height:1;letter-spacing:-0.5px}
.underline{height:3px;width:98px}
.about-title{left:113px;top:825px;color:var(--white)}
.about-line{left:113px;top:866px;background:var(--white)}
.about-text{left:113px;top:896px;width:622px;color:var(--white);font-size:18px;line-height:29px;text-align:justify;font-weight:300}
.read-more{left:113px;top:1071px;width:152px;height:42px;background:var(--white);color:var(--text);font-size:15px}
.about-card{left:790px;top:770px;width:295px;height:385px;border-radius:14px;background:linear-gradient(135deg,#d9d2c7,#e8c9a0)}
.about-photo{left:818px;top:800px;width:242px;height:300px;border:3px solid var(--white);border-radius:12px;background:linear-gradient(160deg,#d8b587 0%,#b98a62 40%,#7fa0c8 80%,#e9e9ef 100%)}
.about-badge{left:806px;top:1097px;width:265px;height:97px;background:var(--brown-dark);border:2px solid var(--white);border-radius:14px;display:flex;align-items:center;justify-content:center}
.about-badge .brand{color:var(--white);font-size:22px}

/* works */
.works-title{left:0;top:1357px;width:1200px;text-align:center}
.works-line{left:551px;top:1399px;background:var(--brown-dark)}
.deco{left:0;top:0;pointer-events:none}
.ph{position:absolute}
.w1{left:163px;top:1524px;width:276px;height:258px;background:linear-gradient(180deg,#c79a6a,#5d6a4a 55%,#2b6fb8 80%,#5b6a3a)}
.w2{left:454px;top:1472px;width:275px;height:259px;background:linear-gradient(180deg,#6e6c6a,#a07a4f 45%,#1d4fa8 75%,#12337a)}
.w3{left:749px;top:1579px;width:275px;height:152px;background:linear-gradient(180deg,#d2d2d0,#6b6560 55%,#2e2925)}
.w4{left:111px;top:1804px;width:328px;height:408px;background:linear-gradient(180deg,#f4f3f1,#d9d6d1 45%,#8a5230 70%,#4a3326)}
.w5{left:456px;top:1749px;width:631px;height:261px;background:linear-gradient(180deg,#d8a673,#8c7d6c 45%,#5b4a38 70%,#4c6a2c)}
.w6{left:457px;top:2027px;width:275px;height:258px;background:linear-gradient(180deg,#ecebea,#8a6a4c 50%,#c6a87f 85%,#3a3a3a)}
.w7{left:749px;top:2027px;width:275px;height:153px;background:linear-gradient(180deg,#f0efee,#d0cecb 60%,#5a4335)}

/* contact */
.contact-band{left:0;top:2440px;width:1200px;height:448px;background:linear-gradient(180deg,#6f584d,#5f4a40 60%,#4e3c33)}
.contact-title{left:132px;top:2490px;color:var(--white)}
.contact-line{left:132px;top:2532px;width:100px;background:var(--white)}
.contact-text{left:132px;top:2558px;width:396px;color:var(--white);font-size:18px;line-height:26px;text-align:justify;font-weight:300}
.social{display:flex;gap:14px}
.social span{width:30px;height:30px;border-radius:50%;display:block}
.dot-a{background:#3b5bb5}
.dot-b{background:#d0397a}
.contact-social{left:130px;top:2712px}
.form-card{left:623px;top:2374px;width:445px;height:441px;background:var(--white);border:1px solid #d9d9d9;border-radius:18px}
.field{left:42px;width:361px;background:var(--field);color:var(--muted);font-size:17px;padding:16px 19px}
.f-email{top:44px;height:52px}
.f-name{top:114px;height:52px}
.f-msg{top:184px;height:142px}
.submit{left:143px;top:358px;width:159px;height:41px;font-size:17px}

/* footer */
.footer-brand{left:113px;top:3022px;font-size:26px}
.fcol{top:2998px;font-size:17px;line-height:29px}
.fcol h4{font-size:17px;font-weight:700;margin-bottom:8px}
.col-company{left:342px}
.col-works{left:531px;top:3000px}
.col-contact{left:723px}
.col-follow{left:1001px}
.col-follow .social{margin-top:6px;gap:8px}
.col-follow .social span{width:24px;height:24px}
.ic{position:absolute;left:-26px}
.footer-rule{left:0;top:3165px;width:1200px;height:1px;background:#e0e0e0}
.copyright{left:0;top:3186px;width:1200px;text-align:center;font-size:15px;color:#555}
</style>
</head>
<body>

<header class="abs site-header">
  <div class="abs brand"><span class="brand-mark"></span>Wade Holloran</div>
  <nav class="abs nav">
    <a class="active" href="#">Home</a>
    <a href="#">About Us</a>
    <a href="#">Contact</a>
  </nav>
  <a class="abs btn btn-accent enquire" href="#">Enquire Us</a>
</header>

<section class="abs hero">
  <div class="abs hero-left" role="img" aria-label="Luxury home back patio with lit windows and swimming pool at dusk"></div>
  <div class="abs hero-right" role="img" aria-label="Large stone and timber custom home exterior at sunset with lawn and fire pit"></div>
  <svg class="abs hero-divider" width="1200" height="560"><line x1="690" y1="0" x2="530" y2="560" stroke="#fff" stroke-width="6"/></svg>
  <h1 class="abs hero-title">WADE HOLLORAN</h1>
  <div class="abs hero-sub">CUSTOM HOMES</div>
  <p class="abs hero-tag">Building beautiful custom homes in Indianapolis for over 20 years</p>
  <a class="abs btn btn-accent get-started" href="#">Get Started</a>
</section>

<section class="abs about"></section>
<h2 class="abs section-title about-title">ABOUT US</h2>
<div class="abs underline about-line"></div>
<p class="abs about-text">Wade Holloran has been building stunning custom homes in the Indianapolis area for over 20 years. As a small boutique building company we only build a handful of homes a year in order to offer our clients the personal attention that their homes deserve. It's this attention to detail that makes our client experience and final product something special and unique.</p>
<a class="abs btn read-more" href="#">Read More</a>
<div class="abs about-card"></div>
<div class="abs about-photo" role="img" aria-label="Family photo of homeowners smiling together outdoors"></div>
<div class="abs about-badge"><div class="brand"><span class="brand-mark"></span>Wade Holloran</div></div>

<svg class="abs deco" width="1200" height="3235">
  <g fill="none" stroke="#b8703f" stroke-width="1.2" stroke-dasharray="4 3">
    <path d="M1185 1266 C1080 1420 900 1512 730 1516"/>
    <path d="M440 1520 C300 1560 80 1680 0 1800"/>
    <path d="M0 1925 C40 1980 80 2030 111 2050"/>
    <path d="M750 2202 C950 2200 1110 2300 1175 2440"/>
    <path d="M1195 1735 L1200 1735"/>
  </g>
</svg>

<h2 class="abs section-title works-title">OUR WORKS</h2>
<div class="abs underline works-line"></div>
<div class="ph w1" role="img" aria-label="Backyard pool and stone house at sunset"></div>
<div class="ph w2" role="img" aria-label="Two-storey rear elevation with lit balcony above pool"></div>
<div class="ph w3" role="img" aria-label="Home bar with stools and wall screens"></div>
<div class="ph w4" role="img" aria-label="White kitchen with gold pendant lights and wood island"></div>
<div class="ph w5" role="img" aria-label="Wide view of a custom home front elevation at dusk"></div>
<div class="ph w6" role="img" aria-label="Dining area with tall windows and wood trim"></div>
<div class="ph w7" role="img" aria-label="Bathroom double vanity with mirrors and sconces"></div>

<section class="abs contact-band" role="img" aria-label="Office desk and chair in muted brown tones"></section>
<h2 class="abs section-title contact-title">CONTACT US</h2>
<div class="abs underline contact-line"></div>
<p class="abs contact-text">Lorem ipsum dolor sit amet, consectetur adipiscing elit, sed do eiusmod tempor incididunt ut labore et dolore magna aliqua. Quis ipsum suspendisse ultrices gravida. Risus commodo viverra maecenas accumsan lacus vel facilisis.</p>
<div class="abs social contact-social"><span class="dot-a"></span><span class="dot-b"></span></div>

<form class="abs form-card">
  <div class="abs field f-email">Email</div>
  <div class="abs field f-name">Name</div>
  <div class="abs field f-msg">Message</div>
  <a class="abs btn btn-accent submit" href="#">Submit</a>
</form>

<footer>
  <div class="abs brand footer-brand"><span class="brand-mark"></span>Wade Holloran</div>
  <div class="abs fcol col-company"><h4>Company</h4>Home<br>About us<br>Contact Us</div>
  <div class="abs fcol col-works"><h4>Our Works</h4>Project 1<br>Project 2</div>
  <div class="abs fcol col-contact"><h4>Contact</h4>
    <div style="position:relative">
      <svg class="ic" style="top:7px" width="12" height="14" viewBox="0 0 12 14"><path d="M6 0a5 5 0 0 0-5 5c0 4 5 9 5 9s5-5 5-9a5 5 0 0 0-5-5zm0 7a2 2 0 1 1 0-4 2 2 0 0 1 0 4z" fill="#2b2b2b"/></svg>
      415 North Fernmill Rd,<br>Suite 308, Carmel IN 46033
    </div>
    <div style="position:relative">
      <svg class="ic" style="top:8px" width="13" height="13" viewBox="0 0 24 24"><path d="M6.6 10.8a15 15 0 0 0 6.6 6.6l2.2-2.2a1 1 0 0 1 1-.25 11 11 0 0 0 3.6.6 1 1 0 0 1 1 1V20a1 1 0 0 1-1 1A17 17 0 0 1 3 4a1 1 0 0 1 1-1h3.5a1 1 0 0 1 1 1 11 11 0 0 0 .6 3.6 1 1 0 0 1-.25 1z" fill="#2b2b2b"/></svg>
      317-552-7190
    </div>
    <div style="position:relative">
      <svg class="ic" style="top:10px" width="13" height="10" viewBox="0 0 13 10"><rect width="13" height="10" fill="#2b2b2b"/><path d="M0 0l6.5 5L13 0" stroke="#fff" fill="none"/></svg>
      wade@whcrafted.com
    </div>
  </div>
  <div class="abs fcol col-follow"><h4>Follow Us</h4><div class="social"><span class="dot-a"></span><span class="dot-b"></span></div></div>
  <div class="abs footer-rule"></div>
  <div class="abs copyright">© Copyrights 2023 Wade Holloran | All Rights Reserved</div>
</footer>

</body>
</html>
```